I need a business Card Design for my practice , i am clinical herbalist. I am a herbalist specializing in Lyme disease, autism, autoimmune diseases, difficult to cure diseasesDifficult to cure diseases. In my innovative practice i link traditional medicine, herbs with science, immunologu ,pharmacology.

Industry/Entity Type

Business

Contact Information for Business Card

My company name : OŚRODEK ZIELNIK
My name : Piotr Kaleta
Name of my profession : Fitoterapeuta
In Polish language Fitoterapeuta is Herbalist .

e-mail: piotrkaleta@osrodekzielnik.com
www.osrodek-zielnik.pl
phone : 604 587 231
My company adress : Dąbrowa Sitnicka 41 , 38-415 Zielinówka
I dont have logo .

Requirements
Nice to have
• My company

```html
<!DOCTYPE html>
<html lang="pl">
<head>
<meta charset="utf-8">
<title>Ośrodek Zielnik – wizytówka</title>
<link rel="stylesheet" href="https://fonts.googleapis.com/css2?family=Fira+Sans:wght@700&display=swap">
<style>
  :root {
    --brand-green: #12883b;
    --paper: #ffffff;
    --page: #ffffff;
  }
  * { margin: 0; padding: 0; box-sizing: border-box; }
  html, body {
    width: 1200px;
    height: 1200px;
    overflow: hidden;
    background: var(--page);
  }
  .canvas {
    position: relative;
    width: 1200px;
    height: 1200px;
    font-family: "Fira Sans", Arial, sans-serif;
    font-weight: 700;
    color: var(--brand-green);
  }
  .business-card {
    position: absolute;
    left: 94px;
    top: 320px;
    width: 1010px;
    height: 560px;
    background: var(--brand-green);
    border-radius: 36px;
  }
  .card-face {
    position: absolute;
    left: 36px;
    top: 36px;
    right: 36px;
    bottom: 36px;
    background: var(--paper);
  }
  .brand-mark {
    position: absolute;
    left: 336px;
    top: 568px;
    width: 300px;
    height: 300px;
    margin: -150px 0 0 -150px;
    border-radius: 50%;
    background: var(--brand-green);
  }
  .brand-name {
    position: absolute;
    left: 357px;
    top: 760px;
    transform: translateX(-50%);
    font-size: 32px;
    line-height: 1;
    white-space: nowrap;
  }
  .details {
    position: absolute;
    left: 636px;
    line-height: 1;
    white-space: nowrap;
  }
  .person-name { top: 420px; font-size: 56px; }
  .person-role { top: 492px; font-size: 21px; }
  .company-name { top: 601px; font-size: 35px; }
  .contact-line { font-size: 21px; }
  .address { top: 650px; }
  .phone { top: 680px; }
  .email { top: 706px; }
  .website { top: 761px; font-size: 27px; }
</style>
</head>
<body>
<main class="canvas">
  <section class="business-card">
    <div class="card-face"></div>
  </section>

  <div class="brand-mark" role="img" aria-label="Znak firmowy Ośrodka Zielnik"></div>
  <p class="brand-name">OŚRODEK ZIELNIK</p>

  <h1 class="details person-name">Piotr Kaleta</h1>
  <p class="details person-role">Fitoterapeuta (Herbalist)</p>

  <h2 class="details company-name">OŚRODEK ZIELNIK</h2>
  <p class="details contact-line address">Dąbrowa Sitnicka 41 , 38-415 Zielinówka</p>
  <p class="details contact-line phone">Phone : 604 587 231</p>
  <p class="details contact-line email">email : piotrkaleta@osrodekzielnik.com</p>
  <p class="details website">www.osrodek-zielnik.pl</p>
</main>
</body>
</html>
```